Handyman Business Card and website logo design

I need a logo for my new handyman business. The logo will be used for my website, business cards, and Facebook pages. I want my business card to have this logo and have a simplistic and nicely flowing design with a handyman feel.

The name of my business is KT Nest Fixer. (Dr is for doctor NOT Drive). So my thoughts for my logo is a handyman with a stethoscope and looking like a doctor examining a house. With handyman will have a tool-belt on and holding a drill or some other well recognized tool. Basically a handyman doctor examining someones "precious home" so that he can prescribe the right "fix" for them.

Contact Information for Business Card

Martin Pellow (CEO)
KTNestFixer
4170 Willowmere Court
Naperville, IL 60571

```html
<!DOCTYPE html>
<html lang="en">
<head>
<meta charset="utf-8">
<title>KT Nest Fixer. — Business Card</title>
<link rel="stylesheet" href="https://fonts.googleapis.com/css2?family=Open+Sans:wght@400;600;700&display=swap">
<style>
  :root {
    --backdrop: #2e3034;
    --brand-blue: #0a6fc2;
    --card-white: #ffffff;
    --logo-grey: #5f6163;
    --text-dark: #1c1c1c;
  }
  * { margin: 0; padding: 0; box-sizing: border-box; }
  html, body {
    width: 1200px;
    height: 864px;
    overflow: hidden;
    background: var(--backdrop);
    font-family: "Open Sans", Arial, sans-serif;
  }
  .card-set {
    position: relative;
    width: 1200px;
    height: 864px;
  }
  .card {
    position: absolute;
    top: 277px;
    width: 540px;
    height: 310px;
    border-radius: 3px;
    overflow: hidden;
  }
  .card--front {
    left: 45px;
    background: var(--brand-blue);
  }
  .card--back {
    left: 615px;
    background: var(--card-white);
  }
  .brand-name {
    position: absolute;
    font-weight: 400;
    letter-spacing: 3px;
    white-space: nowrap;
  }
  .card--front .brand-name {
    right: 48px;
    bottom: 62px;
    font-size: 34px;
    color: var(--card-white);
  }
  .card--back .brand-name {
    left: 40px;
    top: 60px;
    font-size: 38px;
    color: var(--logo-grey);
  }
  .contact {
    position: absolute;
    right: 48px;
    bottom: 40px;
    text-align: right;
  }
  .contact__name {
    font-size: 19px;
    font-weight: 700;
    color: var(--brand-blue);
    line-height: 1.2;
  }
  .contact__role {
    font-size: 14px;
    color: var(--text-dark);
    margin-bottom: 22px;
  }
  .contact__address {
    font-size: 14.5px;
    line-height: 1.5;
    color: var(--text-dark);
    font-style: normal;
  }
</style>
</head>
<body>
  <main class="card-set">
    <section class="card card--front" aria-label="Card front">
      <p class="brand-name">KT Nest Fixer.</p>
    </section>

    <section class="card card--back" aria-label="Card back">
      <p class="brand-name">KT Nest Fixer.</p>
      <div class="contact">
        <p class="contact__name">Martin Pellow</p>
        <p class="contact__role">CEO</p>
        <address class="contact__address">
          4170 Willowmere Court<br>
          Naperville, IL 60571
        </address>
      </div>
    </section>
  </main>
</body>
</html>
```